RM Cargoline businesscard project

RM Cargoline Ltd is a freshly founded small (3 employees), young (average age is 30 years) company, living from the road transportation market without own tools.
We would like to have an impressive, new-line, cool busines card for a freshly founded forwarding company on an overcrowded market which raises attention and makes the potential partners eager to work with us.

Target Market(s)

The main profile of the company is logistic/forwarding on road.

Industry/Entity Type

Freight Forwarding

Contact Information for Business Card

Name: Berki Zsófia
Title: general manager
mobile nr: +36-70/482-5193
fax nr: +36-1/534-9061
e-mail: zsofia.berki@rmcargoline.example
info@rmcargoline.example
website address: http://www.rmcargoline.example
and if possible maybe some funny or helpful info on the back

Requirements
Must have
• contact details above
Nice to have
• some really nice and catching back-side (info, graphics, useful tool info... anything)
Should not have
• trucks, road, ship, airplane on it...

```html
<!DOCTYPE html>
<html lang="hu">
<head>
<meta charset="utf-8">
<title>RM Velmora – Business Card</title>
<link rel="stylesheet" href="https://fonts.googleapis.com/css2?family=Arimo:wght@400;700&display=swap">
<style>
  :root {
    --backdrop: #2b2b2b;
    --card: #ffffff;
    --ink: #1c1c1c;
    --accent: #4a7cc0;
  }
  * { margin: 0; padding: 0; box-sizing: border-box; }
  html, body {
    width: 1200px;
    height: 900px;
    overflow: hidden;
    background: var(--backdrop);
    font-family: "Arimo", Arial, sans-serif;
  }
  .stage {
    width: 1200px;
    height: 900px;
    display: flex;
    align-items: center;
    justify-content: center;
  }
  .business-card {
    position: relative;
    width: 900px;
    height: 560px;
    background: var(--card);
    box-shadow: 0 10px 30px rgba(0,0,0,.35);
  }
  .brand {
    position: absolute;
    left: 72px;
    top: 82px;
  }
  .brand-square {
    width: 64px;
    height: 64px;
    background: var(--accent);
  }
  .brand-name {
    margin-top: 34px;
    font-size: 40px;
    font-weight: 400;
    color: var(--ink);
    letter-spacing: -0.5px;
    white-space: nowrap;
  }
  .person {
    position: absolute;
    right: 62px;
    top: 92px;
    text-align: right;
    color: var(--ink);
  }
  .person-name {
    font-size: 44px;
    font-weight: 700;
    line-height: 1.1;
  }
  .person-title {
    font-size: 31px;
    font-weight: 400;
    margin-top: 4px;
    margin-right: 10px;
  }
  .contact-list {
    list-style: none;
    margin-top: 34px;
  }
  .contact-item {
    display: flex;
    align-items: center;
    justify-content: flex-end;
    gap: 14px;
    font-size: 25px;
    line-height: 40px;
    white-space: nowrap;
  }
  .contact-icon {
    width: 26px;
    height: 26px;
    flex: none;
    fill: var(--accent);
  }
</style>
</head>
<body>
<main class="stage">
  <section class="business-card">
    <div class="brand">
      <div class="brand-square"></div>
      <div class="brand-name">RM Velmora</div>
    </div>

    <div class="person">
      <div class="person-name">Berki Zsófia</div>
      <div class="person-title">General Manager</div>
      <ul class="contact-list">
        <li class="contact-item">
          <span>+36-70/482-5193</span>
          <svg class="contact-icon" viewBox="0 0 24 24" aria-label="mobile"><path d="M7 1h10a2 2 0 0 1 2 2v18a2 2 0 0 1-2 2H7a2 2 0 0 1-2-2V3a2 2 0 0 1 2-2zm0 3v14h10V4H7zm5 15.5a1.2 1.2 0 1 0 0 2.4 1.2 1.2 0 0 0 0-2.4z"/></svg>
        </li>
        <li class="contact-item">
          <span>+36-1/534-9061</span>
          <svg class="contact-icon" viewBox="0 0 24 24" aria-label="fax"><path d="M6 2h9l3 3v4H6V2zm-3 8h18a2 2 0 0 1 2 2v6h-4v4H5v-4H1v-6a2 2 0 0 1 2-2zm4 6v4h10v-4H7z"/></svg>
        </li>
        <li class="contact-item">
          <span>zsofia.berki@rmvelmora.example</span>
          <svg class="contact-icon" viewBox="0 0 24 24" aria-label="email"><path d="M2 5h20v14H2V5zm2 2v.4l8 5.6 8-5.6V7H4z"/></svg>
        </li>
        <li class="contact-item">
          <span>info@rmvelmora.example</span>
          <svg class="contact-icon" viewBox="0 0 24 24" aria-label="email"><path d="M2 5h20v14H2V5zm2 2v.4l8 5.6 8-5.6V7H4z"/></svg>
        </li>
        <li class="contact-item">
          <span>www.rmvelmora.example</span>
          <svg class="contact-icon" viewBox="0 0 24 24" aria-label="website"><path d="M12 1a11 11 0 1 0 0 22 11 11 0 0 0 0-22zm0 2c1.3 0 2.6 2.4 3.1 6H8.9C9.4 5.4 10.7 3 12 3zM4.2 9h2.7a20 20 0 0 0 0 6H4.2a9 9 0 0 1 0-6zm4.7 0h6.2a18 18 0 0 1 0 6H8.9a18 18 0 0 1 0-6zm8.2 0h2.7a9 9 0 0 1 0 6h-2.7a20 20 0 0 0 0-6zM8.9 17h6.2c-.5 3.6-1.8 4-3.1 4s-2.6-.4-3.1-4z"/></svg>
        </li>
      </ul>
    </div>
  </section>
</main>
</body>
</html>
```